Nutrition Infographic for weight loss- key points and nutrition habits for after weight loss surgery

I need someone to put together some infographics based on some nutrition information I have put together. We are a company who do weight loss surgery for patients and I am trying to put together some resources for patients so they can look after their nutrition for the long term.

I have some info and ideas on how we can execute this on paper but I need some a creative genius with top notch design skills to help me put it together.

I am basically after two infographics- One with the nutrition information I have outlined and One with the pyramid I have illustrated. Please let me know if you need clarification on the layout. Also happy to take on board any ideas you might have too!

If more time is needed with adjustments/refinements I understand and am happy to work with you to get to a final product we are happy with.

Target Market(s)

weight loss clients- ages ranging mostly from 20-45 male and female.

Industry/Entity Type

Health Care

Colors

Designer to choose colors to be used in the design.

Requirements
Must have
• Simple, clean concepts and images are needed.
• Easy to understand layout to enhance uptake of understanding the information

```html
<!DOCTYPE html>
<html lang="en">
<head>
<meta charset="utf-8">
<title>Nutrition Pyramid for Bariatric Surgery</title>
<link href="https://fonts.googleapis.com/css2?family=Rye&family=Crimson+Text:wght@400;700&display=swap" rel="stylesheet">
<style>
  :root {
    --bg-light: #a9da00;
    --bg-mid: #8fc000;
    --bg-dark: #5c9300;
    --ink: #141a0a;
    --tier-green: #7ccb00;
    --tier-black: #050505;
    --label-white: #ffffff;
    --hourglass-frame: #3d5b5b;
    --sand: #f26a24;
    --drop-blue: #2c8bd2;
    --clock-face: #f4f4f4;
    --clock-inner: #d6d6d6;
    --clock-hand: #3a3a3a;
    --cutlery: #f2f2f2;
  }
  html, body {
    margin: 0;
    padding: 0;
    width: 1200px;
    height: 1200px;
    overflow: hidden;
  }
  .poster {
    display: block;
    width: 1200px;
    height: 1200px;
  }
  .title {
    font-family: "Rye", serif;
    font-size: 62px;
    fill: var(--ink);
  }
  .tip {
    font-family: "Crimson Text", serif;
    font-size: 38px;
    fill: var(--ink);
  }
  .tier-label {
    font-family: "Crimson Text", serif;
    font-size: 20px;
    fill: var(--label-white);
  }
  .tier-label-small {
    font-family: "Crimson Text", serif;
    font-size: 7px;
    font-weight: 700;
    fill: var(--label-white);
  }
</style>
</head>
<body>
<svg class="poster" viewBox="0 0 1200 1200" xmlns="http://www.w3.org/2000/svg">
  <defs>
    <linearGradient id="bg-gradient" x1="0" y1="0" x2="1" y2="1">
      <stop offset="0" stop-color="var(--bg-light)"/>
      <stop offset="0.5" stop-color="var(--bg-mid)"/>
      <stop offset="1" stop-color="var(--bg-dark)"/>
    </linearGradient>
  </defs>

  <rect class="background" width="1200" height="1200" fill="url(#bg-gradient)"/>

  <text class="title" x="606" y="148" text-anchor="middle" textLength="1128" lengthAdjust="spacingAndGlyphs">NUTRITION PYRAMID FOR BARIATRIC SURGERY</text>

  <!-- Eat slowly -->
  <g class="icon-hourglass">
    <rect x="118" y="244" width="92" height="7" rx="3" fill="var(--hourglass-frame)"/>
    <rect x="118" y="345" width="92" height="7" rx="3" fill="var(--hourglass-frame)"/>
    <rect x="124" y="250" width="6" height="96" fill="var(--hourglass-frame)"/>
    <rect x="198" y="250" width="6" height="96" fill="var(--hourglass-frame)"/>
    <path d="M138 252 L190 252 L166 298 L190 344 L138 344 L162 298 Z" fill="none" stroke="var(--hourglass-frame)" stroke-width="4"/>
    <path d="M150 276 L178 276 L164 296 Z" fill="var(--sand)"/>
    <path d="M164 300 L186 341 L142 341 Z" fill="var(--sand)"/>
  </g>
  <text class="tip" x="174" y="401" text-anchor="middle">Eat slowly</text>

  <!-- Hydration -->
  <g class="icon-drop">
    <path d="M164 444 C150 480 118 510 118 545 A46 46 0 0 0 210 545 C210 510 178 480 164 444 Z" fill="var(--drop-blue)"/>
    <path d="M164 478 C154 502 138 522 138 545 A26 26 0 0 0 190 545 C190 522 174 502 164 478 Z" fill="none" stroke="var(--bg-mid)" stroke-width="5"/>
    <circle cx="171" cy="549" r="8" fill="var(--drop-blue)"/>
    <circle cx="161" cy="526" r="4" fill="var(--drop-blue)"/>
  </g>
  <text class="tip" x="201" y="637" text-anchor="middle">Good hydration with</text>
  <text class="tip" x="196" y="679" text-anchor="middle">water (2 litres +)</text>

  <!-- Healthy fats -->
  <rect class="illustration-oils" x="74" y="770" width="202" height="120" rx="10" fill="#c9c46a" role="img" aria-label="Four bottles of olive, sesame, almond and sunflower oil"/>
  <text class="tip" x="155" y="945" text-anchor="middle">Include some</text>
  <text class="tip" x="142" y="987" text-anchor="middle">healthy</text>
  <text class="tip" x="150" y="1029" text-anchor="middle">essential fats</text>

  <!-- Regular meals -->
  <g class="icon-meal-clock">
    <ellipse cx="944" cy="276" rx="10" ry="14" fill="var(--cutlery)"/>
    <rect x="941" y="286" width="6" height="66" rx="3" fill="var(--cutlery)"/>
    <circle cx="1011" cy="312" r="50" fill="var(--clock-face)"/>
    <circle cx="1011" cy="312" r="30" fill="var(--clock-inner)"/>
    <line x1="1011" y1="312" x2="986" y2="296" stroke="var(--clock-hand)" stroke-width="7" stroke-linecap="round"/>
    <line x1="1011" y1="312" x2="1030" y2="300" stroke="var(--clock-hand)" stroke-width="7" stroke-linecap="round"/>
    <rect x="1072" y="252" width="7" height="100" rx="3" fill="var(--cutlery)"/>
    <rect x="1086" y="262" width="14" height="28" rx="4" fill="var(--cutlery)"/>
    <rect x="1090" y="286" width="6" height="66" rx="3" fill="var(--cutlery)"/>
  </g>
  <text class="tip" x="1006" y="413" text-anchor="middle">Aim for regular</text>
  <text class="tip" x="1006" y="455" text-anchor="middle">meal and snacks</text>

  <!-- Supplements -->
  <rect class="illustration-supplements" x="948" y="576" width="106" height="72" rx="8" fill="#d4e4ef" role="img" aria-label="Vitamin bottle and blister pack of capsules"/>
  <text class="tip" x="1012" y="686" text-anchor="middle">Take daily vitamins</text>
  <text class="tip" x="996" y="728" text-anchor="middle">and mineral</text>
  <text class="tip" x="1002" y="770" text-anchor="middle">supplements</text>

  <!-- Physical activity -->
  <rect class="illustration-exercise" x="944" y="828" width="212" height="164" rx="10" fill="#4a6e12" role="img" aria-label="Silhouettes of people lifting weights and stretching"/>
  <text class="tip" x="956" y="1032">Keep physically</text>
  <text class="tip" x="1062" y="1074" text-anchor="middle">active</text>

  <!-- Pyramid -->
  <g class="pyramid">
    <polygon class="tier tier-grains" points="596,430 668,558 524,558" fill="var(--tier-black)"/>
    <rect x="572" y="500" width="50" height="50" rx="5" fill="#3a2a14" role="img" aria-label="Bread, toast, rice, corn and pasta"/>
    <text class="tier-label-small" x="597" y="471" text-anchor="middle">Whole grains</text>
    <text class="tier-label-small" x="597" y="479" text-anchor="middle">Quality carbs</text>

    <polygon class="tier tier-fruits" points="494,568 678,568 742,684 450,684" fill="var(--tier-green)"/>
    <rect x="488" y="600" width="206" height="78" rx="8" fill="#c7423a" opacity="0.55" role="img" aria-label="Banana, apple, orange, pear, strawberry, grapes, watermelon and cherries"/>
    <text class="tier-label" x="527" y="592">Fruits</text>

    <polygon class="tier tier-vegetables" points="432,698 752,698 816,814 376,814" fill="var(--tier-black)"/>
    <rect x="420" y="732" width="350" height="74" rx="8" fill="#3f6f1e" opacity="0.8" role="img" aria-label="Eggplant, broccoli, lettuce, cucumber, carrot, tomato, cauliflower, radish, asparagus and pepper"/>
    <text class="tier-label" x="437" y="724">Vegetables</text>

    <polygon class="tier tier-proteins" points="336,826 590,826 590,1072 230,1072" fill="var(--tier-green)"/>
    <rect x="330" y="866" width="250" height="200" rx="10" fill="#e07a5a" opacity="0.55" role="img" aria-label="Salmon, prawn, fish, chicken, steak and eggs"/>
    <text class="tier-label" x="369" y="855">High quality proteins</text>

    <polygon class="tier tier-dairy" points="602,826 824,826 890,942 602,942" fill="var(--tier-black)"/>
    <rect x="622" y="856" width="210" height="80" rx="8" fill="#e8d36a" opacity="0.6" role="img" aria-label="Milk, yoghurt, cream and cheeses"/>
    <text class="tier-label" x="611" y="847">Dairy products</text>

    <polygon class="tier tier-nuts" points="602,956 900,956 964,1072 602,1072" fill="var(--tier-black)"/>
    <rect x="610" y="986" width="296" height="80" rx="8" fill="#9a6a3a" opacity="0.7" role="img" aria-label="Cashews, almonds, walnuts, pistachios and seeds"/>
    <text class="tier-label" x="611" y="980">Dry fruits and seeds</text>
  </g>
</svg>
</body>
</html>
```